Upsell Vertical Banner Ad Design For B2B Marketing Agency Vertical 768px × 1180px IS THE SIZE

I need a banner made for my website www.brightlanepromotionhub.biz This banner will be an upsell advertisement for after someone signs up for my monthly program. When they login to their account for the 1st time I will give them the chance to upgrade their account to our annual program with just one click.

this is a page that upsells it currently to give you an idea how we market ourselves:
https://tlpx.pagevault-example.com/page/tlp-annual-upsell

Use this content:

Are You Ready To Commit To Taking Your Business To The Next Level?

Because We're In This For The Long-Haul and Dedicated To Your Success...

Save $300 By Upgrading To An Annual Membership And Pay Only $74/mth

((BUTTON))Yes, Upgrade My Plan Right Now!

*Must prepay the full year at only $898/yr!

Target Market(s)

business owners

Industry/Entity Type

Marketing

Requirements
Must have
• 768px × 1180px IS THE SIZE vertical

Use this content:

Nice to have
• Use this content:

Should not have
• Use this content:

```html
<!DOCTYPE html>
<html lang="en">
<head>
<meta charset="utf-8">
<title>Annual Membership Upgrade Banner</title>
<link href="https://fonts.googleapis.com/css2?family=Source+Sans+3:wght@400;600;700;800&display=swap" rel="stylesheet">
<style>
  :root {
    --ink: #0d0d0d;
    --white: #ffffff;
    --accent: #2aa3e0;
    --blue-deep: #3a8bcf;
    --blue-mid: #3fb4e0;
    --cyan-light: #8ff8fb;
    --teal: #22c9e6;
    --teal-deep: #2c8fd0;
    --mist: #bfe3f3;
  }
  html, body {
    margin: 0;
    padding: 0;
    width: 781px;
    height: 1200px;
    overflow: hidden;
    background: var(--white);
  }
  .canvas {
    position: relative;
    width: 781px;
    height: 1200px;
    overflow: hidden;
  }
  .banner {
    position: absolute;
    left: 0;
    top: 0;
    width: 768px;
    height: 1180px;
    transform: scale(1.0169);
    transform-origin: 0 0;
    font-family: "Source Sans 3", "Myriad Pro", sans-serif;
    color: var(--ink);
  }
  .backdrop {
    position: absolute;
    inset: 0;
    width: 768px;
    height: 1180px;
  }
  .line {
    position: absolute;
    margin: 0;
    line-height: 1;
    white-space: nowrap;
  }
  .headline-main {
    left: 46px;
    top: 118px;
    font-size: 92px;
    font-weight: 700;
    letter-spacing: -1px;
  }
  .headline-sub {
    left: 50px;
    font-size: 58px;
    font-weight: 400;
    letter-spacing: -0.5px;
  }
  .headline-sub.l1 { top: 222px; }
  .headline-sub.l2 { top: 287px; }
  .headline-sub.l3 { top: 352px; }
  .hl-white { color: var(--white); font-weight: 600; }
  .hl-bold { font-weight: 700; }
  .tagline {
    left: 48px;
    font-size: 20px;
  }
  .tagline.l1 { top: 444px; }
  .tagline.l2 { top: 469px; }

  .offer .line { right: 50px; text-align: right; }
  .offer-save { top: 474px; font-size: 56px; font-weight: 700; }
  .offer-amount { top: 526px; font-size: 84px; font-weight: 700; color: var(--accent); letter-spacing: -1px; }
  .offer-text { font-size: 40px; }
  .offer-text.t1 { top: 608px; }
  .offer-text.t2 { top: 658px; }
  .offer-plan { top: 718px; font-size: 40px; font-weight: 600; color: var(--accent); }
  .offer-text.t3 { top: 768px; }
  .offer-text.t4 { top: 818px; }
  .offer-price { top: 870px; font-size: 40px; font-weight: 700; }

  .cta {
    left: 0;
    width: 730px;
    text-align: center;
    top: 972px;
    font-size: 22px;
  }
  .terms {
    left: 0;
    width: 745px;
    text-align: center;
    font-size: 32px;
    font-weight: 600;
  }
  .terms.l1 { top: 1030px; }
  .terms.l2 { top: 1074px; }
</style>
</head>
<body>
<div class="canvas">
  <div class="banner">
    <svg class="backdrop" viewBox="0 0 768 1180" aria-hidden="true">
      <defs>
        <linearGradient id="bg-sweep" x1="0" y1="1" x2="1" y2="0">
          <stop offset="0" stop-color="var(--blue-deep)"/>
          <stop offset="0.45" stop-color="var(--blue-mid)"/>
          <stop offset="1" stop-color="var(--cyan-light)"/>
        </linearGradient>
        <linearGradient id="band-sweep" x1="0" y1="0" x2="1" y2="0.6">
          <stop offset="0" stop-color="var(--mist)"/>
          <stop offset="0.55" stop-color="#7fd8ee"/>
          <stop offset="1" stop-color="#55e3f3"/>
        </linearGradient>
        <linearGradient id="corner-sweep" x1="0" y1="1" x2="1" y2="0">
          <stop offset="0" stop-color="var(--teal)"/>
          <stop offset="1" stop-color="var(--cyan-light)"/>
        </linearGradient>
        <linearGradient id="corner-deep" x1="0" y1="1" x2="1" y2="0">
          <stop offset="0" stop-color="var(--teal-deep)"/>
          <stop offset="1" stop-color="var(--teal)"/>
        </linearGradient>
      </defs>
      <rect width="768" height="1180" fill="url(#bg-sweep)"/>
      <polygon points="768,285 330,735 90,970 300,1180 768,1180" fill="var(--white)"/>
      <polygon points="330,735 90,970 300,1180 560,1040" fill="url(#band-sweep)"/>
      <polygon points="90,970 0,1060 0,1180 300,1180" fill="var(--white)"/>
      <polygon points="768,955 600,1120 660,1180 768,1180" fill="url(#corner-sweep)"/>
      <polygon points="768,1060 650,1180 768,1180" fill="url(#corner-deep)"/>
    </svg>

    <h1 class="line headline-main">ARE YOU READY</h1>
    <p class="line headline-sub l1">To <span class="hl-white">Commit</span> To <span class="hl-white">Taking</span></p>
    <p class="line headline-sub l2">Your Business</p>
    <p class="line headline-sub l3">To The <span class="hl-bold">Next Level</span>?</p>

    <p class="line tagline l1">Because We're In This For The Long-Haul</p>
    <p class="line tagline l2">and Dedicated To Your Success...</p>

    <div class="offer">
      <p class="line offer-save">Save</p>
      <p class="line offer-amount">$300</p>
      <p class="line offer-text t1">By Upgrading</p>
      <p class="line offer-text t2">To An</p>
      <p class="line offer-plan">Annual Membership</p>
      <p class="line offer-text t3">And</p>
      <p class="line offer-text t4">Pay Only</p>
      <p class="line offer-price">$74/mth</p>
    </div>

    <p class="line cta">Yes, Upgrade My Plan Right Now!</p>
    <p class="line terms l1">MUST PREPAY THE FULL YEAR</p>
    <p class="line terms l2">AT ONLY $898/YR!</p>
  </div>
</div>
</body>
</html>
```